PPT template for boutique strategic planning, accounting and taxation firm

We are a boutique firm that provides strategic, accounting and tax advice to our clients. The work we are doing is increasingly strategic work and we are required to produce reports and presentations and our current templates are simply not sufficient.
As you can see from the examples attached, we have very limited skills in house re design! We have attached a PPT document and word document (that should be PPT) that we use regularly as examples of the content. Excel worksheets are regularly embedded into the presentation (in both blue and orange - see below re colours)
Not specific to one area but typically these clients are famous for their own brand and are creating value in their industry through creating their own brand and we want to produce documents of a similar standard.
A Powerpoint Document Slide Template
Cover page layout, back page, intermediate page heading, in colours and styles based on the logo, title styles, and an intermediate or chapter heading slide style. Many of our presentations contain slides with tables, diagrams, flowcharts and text, including simple lists of bullet points. As above, you will see in our style guide that we have three coloured logos – we would like one version in blue and one version in orange please. Again, the cover should be bold and draw attention but remain professional.
We are looking for something that works in both 4:3 and 16:9 (or two templates please)
We like a clear professional and simple look.
Deliverable: PowerPoint template file (.potx extension) for PowerPoint 2007 with at least a “cover” layout, a “title and content” layout, and a simplified slide layout, as well as “back cover”. Please embed any fonts used.
Target Market(s)
Many of our clients are retail clients or have strong brands of their own.
Industry/Entity Type
Accounting
Requirements
Must have
- Harrowby & Co logo on each page.
Must have a cover page (please be bold but professional)
A selection of "standard" slides - dot points, detailed written content, example diagrams, flow charts etc.
A back cover
Nice to have
- We would like to have a copy done in both the blue and orange versions attached. Happy for the winner to complete the other colour after the winner is selected.
Prefer Arial logo but open to suggestions. Must be easy to read and professional
Should not have
- Nothing cartoonish

```html
<!DOCTYPE html>
<html lang="en">
<head>
<meta charset="utf-8">
<title>Harrowby &amp; Co – Business Improvement Slide Template</title>
<link rel="stylesheet" href="https://fonts.googleapis.com/css2?family=Montserrat:ital,wght@0,300;0,400;0,600;0,700;0,800;1,400&display=swap">
<style>
  :root{
    --page:#3a3a3a;
    --slide-top:#f1f2f4;
    --slide-bottom:#dadde1;
    --blue:#0b5db3;
    --blue-dark:#134a86;
    --blue-mid:#2a7dd1;
    --teal:#14a6a6;
    --orange:#f07f22;
    --ink:#3d4450;
    --ink-soft:#6b717a;
    --white:#ffffff;
  }
  *{box-sizing:border-box;margin:0;padding:0}
  html,body{width:759px;height:1200px;overflow:hidden;background:var(--page)}
  body{position:relative;font-family:"Montserrat",Arial,sans-serif;color:var(--ink)}
  .slide{position:absolute;width:363px;height:226px;overflow:hidden;
    background:linear-gradient(180deg,var(--slide-top),var(--slide-bottom))}
  .col-l{left:12px}.col-r{left:385px}
  .row-1{top:15px}.row-2{top:251px}.row-3{top:486px}.row-4{top:721px}.row-5{top:957px}

  .slide-header{position:absolute;left:0;top:0;width:100%;height:17px;
    background:linear-gradient(90deg,var(--blue),var(--teal));padding:3px 0 0 31px;color:var(--white)}
  .slide-header h2{font-size:5.6px;font-weight:700;letter-spacing:.1px;line-height:6px;text-transform:uppercase}
  .slide-header p{font-size:3.4px;line-height:4px;opacity:.85}

  .slide-footer{position:absolute;left:0;top:205px;width:100%;height:17px}
  .page-no{position:absolute;left:0;top:0;width:34px;height:17px;border-radius:0 9px 9px 0;
    background:var(--blue);color:var(--white);font-size:8px;font-weight:600;padding:3px 0 0 10px}
  .footer-bar{position:absolute;left:128px;right:0;top:0;height:17px;border-radius:9px 0 0 9px;
    background:linear-gradient(90deg,var(--blue),var(--teal));color:var(--white);
    font-size:4.6px;font-style:italic;text-align:right;padding:6px 12px 0 0}

  .brand{position:absolute;display:flex;align-items:center;gap:3px}
  .brand-dot{flex:none;border-radius:50%;background:var(--blue)}
  .brand-name{font-weight:700;color:var(--blue);white-space:nowrap;letter-spacing:-.2px}
  .brand-tag{color:var(--blue);white-space:nowrap}
  .slide-footer .brand{left:40px;top:1.5px}
  .slide-footer .brand-dot{width:13px;height:13px}
  .slide-footer .brand-name{font-size:7.2px;line-height:8px}
  .slide-footer .brand-tag{font-size:2.2px;line-height:3px}

  /* cover */
  .cover-pill-l{position:absolute;left:0;top:111px;width:38px;height:25px;border-radius:0 13px 13px 0;background:var(--blue)}
  .cover-pill-r{position:absolute;left:179px;right:0;top:111px;height:25px;border-radius:13px 0 0 13px;
    background:linear-gradient(90deg,var(--blue),var(--teal))}
  .cover .brand{left:46px;top:111px}
  .cover .brand-dot{width:24px;height:24px}
  .cover .brand-name{font-size:11.5px;line-height:13px}
  .cover .brand-tag{font-size:3.2px;line-height:4px}

  /* title */
  .title-block{position:absolute;left:107px;top:74px;color:var(--blue);line-height:.95}
  .title-block .t-the{font-size:19px;font-weight:600}
  .title-block .t-main{font-size:30px;font-weight:800;letter-spacing:-.3px}
  .title-block .t-sub{font-size:21px;font-weight:700}
  .title-block .t-intro{font-size:14px;font-weight:300;color:var(--blue-mid)}

  /* table */
  .table-title{position:absolute;left:64px;top:43px;font-size:4.6px;font-weight:700}
  table.clients{position:absolute;left:64px;top:50px;width:243px;border-collapse:collapse;background:var(--white);
    font-size:2.6px;color:var(--ink-soft)}
  table.clients th{background:var(--blue);color:var(--white);font-size:4.2px;font-weight:400;height:14px;line-height:4.4px}
  table.clients td{height:11.5px;padding-left:3px;border-bottom:.5px solid #e3e5e8}
  .table-date{position:absolute;left:244px;top:185px;font-size:3.6px;color:var(--ink-soft)}

  /* bullets */
  .bullets{position:absolute;list-style:none}
  .bullets li{position:relative;font-size:5.8px;height:17px;color:var(--ink-soft)}
  .bullets li::before{content:"";position:absolute;left:-17px;top:1px;width:4px;height:4px;border-radius:50%;background:var(--orange)}
  .bullets-wide{left:69px;top:51px}
  .bullets-side{left:201px;top:61px}
  .photo{position:absolute;left:21px;top:64px;width:121px;height:101px;
    background:linear-gradient(160deg,#e9ecef,#b9c2cc 60%,#8d99a6);box-shadow:0 3px 6px rgba(0,0,0,.2)}
  .divider{position:absolute;left:179px;top:56px;width:.7px;height:115px;background:#b8bec6}

  .body-svg{position:absolute;left:0;top:17px;width:363px;height:188px}
  .body-svg text{font-family:"Montserrat",Arial,sans-serif}
</style>
</head>
<body>

<!-- 1 cover -->
<section class="slide cover col-l row-1">
  <div class="cover-pill-l"></div>
  <div class="brand">
    <span class="brand-dot"></span>
    <div><div class="brand-name">Harrowby &amp; Co</div><div class="brand-tag">Accounting, Taxation &amp; Strategic Business Advisers</div></div>
  </div>
  <div class="cover-pill-r"></div>
</section>

<!-- 2 title -->
<section class="slide col-r row-1">
  <div class="title-block">
    <div class="t-the">The</div>
    <div class="t-main">Business</div>
    <div class="t-sub">Improvement</div>
    <div class="t-intro">Process an introduction</div>
  </div>
</section>

<!-- 3 clients table -->
<section class="slide col-l row-2">
  <header class="slide-header"><h2>Some of our clients</h2><p>subtitle write Here</p></header>
  <div class="table-title">1. Name of Table goes here</div>
  <table class="clients">
    <tr><th>Professional<br>services</th><th>Transport</th><th>Distribution</th><th>Property /<br>Construction</th><th>Retail</th><th>Manufacturing</th></tr>
    <tr><td>Service item 1</td><td>Bus</td><td>Armenia</td><td>Property name</td><td>Retail name here</td><td>Norvale</td></tr>
    <tr><td>Service item 2</td><td>Truck</td><td>Brazil</td><td>Property name</td><td>Retail name here</td><td>Kestra</td></tr>
    <tr><td>Service item 3</td><td>Train</td><td>Japan</td><td>Property name</td><td>Retail name here</td><td>Dunmore</td></tr>
    <tr><td>Service item 4</td><td>Plane</td><td>Norway</td><td>Property name</td><td>Retail name here</td><td>Acrelo</td></tr>
    <tr><td>Service item 5</td><td>Ship</td><td>Indonesia</td><td>Property name</td><td>Retail name here</td><td>Tamsin</td></tr>
    <tr><td>Service item 6</td><td>Boat</td><td>Philippines</td><td>Property name</td><td>Retail name here</td><td>Belvo</td></tr>
    <tr><td>Service item 7</td><td>Car</td><td>Thailand</td><td>Property name</td><td>Retail name here</td><td>Orrin</td></tr>
    <tr><td>Service item 8</td><td>Motorcycle</td><td>Canada</td><td>Property name</td><td>Retail name here</td><td>Velmar</td></tr>
    <tr><td>Service item 9</td><td>Van</td><td>Chile</td><td>Property name</td><td>Retail name here</td><td>Holtby</td></tr>
    <tr><td>Service item 10</td><td>Other</td><td>Korea</td><td>Property name</td><td>Retail name here</td><td>Prisma</td></tr>
  </table>
  <div class="table-date">January 10, 2014</div>
  <footer class="slide-footer"><div class="page-no">3</div><div class="brand"><span class="brand-dot"></span><div><div class="brand-name">Harrowby &amp; Co</div><div class="brand-tag">Accounting, Taxation &amp; Strategic Business Advisers</div></div></div><div class="footer-bar">The business improvement process – an introduction</div></footer>
</section>

<!-- 4 principles -->
<section class="slide col-r row-2">
  <header class="slide-header"><h2>Key success principles</h2><p>subtitle write Here</p></header>
  <ul class="bullets bullets-wide">
    <li>Find and work with a trusted business advisor</li>
    <li>Understand and drive economic value creation</li>
    <li>Measure and improve free cash flow</li>
    <li>Identify and improve the economic denominator</li>
    <li>Sharpen and maintain focus</li>
    <li>Measure and improve processes</li>
    <li>Limit the number of strategic goals</li>
  </ul>
  <footer class="slide-footer"><div class="page-no">4</div><div class="brand"><span class="brand-dot"></span><div><div class="brand-name">Harrowby &amp; Co</div><div class="brand-tag">Accounting, Taxation &amp; Strategic Business Advisers</div></div></div><div class="footer-bar">The business improvement process – an introduction</div></footer>
</section>

<!-- 5 principles with image -->
<section class="slide col-l row-3">
  <header class="slide-header"><h2>Key success principles</h2><p>with image</p></header>
  <div class="photo" role="img" aria-label="Photo of a business team meeting around a whiteboard"></div>
  <div class="divider"></div>
  <ul class="bullets bullets-side">
    <li>Find and work with a trusted business advisor</li>
    <li>Understand and drive economic value creation</li>
    <li>Measure and improve free cash flow</li>
    <li>Identify and improve the economic denominator</li>
    <li>Sharpen and maintain focus</li>
    <li>Measure and improve processes</li>
    <li>Limit the number of strategic goals</li>
  </ul>
  <footer class="slide-footer"><div class="page-no">4</div><div class="brand"><span class="brand-dot"></span><div><div class="brand-name">Harrowby &amp; Co</div><div class="brand-tag">Accounting, Taxation &amp; Strategic Business Advisers</div></div></div><div class="footer-bar">The business improvement process – an introduction</div></footer>
</section>

<!-- 6 entrepreneur value -->
<section class="slide col-r row-3">
  <header class="slide-header"><h2>The value of the entrepreneur</h2><p>subtitle write Here</p></header>
  <svg class="body-svg" viewBox="0 0 363 188">
    <rect x="31" y="23" width="178" height="31" fill="var(--blue)"/>
    <path d="M44 54 L44 66 L58 54 Z" fill="var(--blue)"/>
    <text x="42" y="42" font-size="8.2" fill="#fff">Entrepreneurial <tspan font-weight="700">abilities</tspan> create wealth</text>
    <rect x="160" y="72" width="178" height="28" fill="var(--teal)"/>
    <path d="M318 100 L332 110 L332 100 Z" fill="var(--teal)"/>
    <text x="170" y="89" font-size="8.2" fill="#fff">Entrepreneurial <tspan font-weight="700">attitudes</tspan> create wealth</text>
    <rect x="67" y="121" width="186" height="28" fill="var(--orange)"/>
    <path d="M80 149 L80 161 L94 149 Z" fill="var(--orange)"/>
    <text x="76" y="138" font-size="8.2" fill="#fff">Entrepreneurial <tspan font-weight="700">behaviours</tspan> create wealth</text>
  </svg>
  <footer class="slide-footer"><div class="page-no">5</div><div class="brand"><span class="brand-dot"></span><div><div class="brand-name">Harrowby &amp; Co</div><div class="brand-tag">Accounting, Taxation &amp; Strategic Business Advisers</div></div></div><div class="footer-bar">The business improvement process – an introduction</div></footer>
</section>

<!-- 7 what is entrepreneurship -->
<section class="slide col-l row-4">
  <header class="slide-header"><h2>What is entrepreneurship</h2><p>subtitle write Here</p></header>
  <svg class="body-svg" viewBox="0 0 363 188">
    <ellipse cx="95" cy="35" rx="42" ry="29" fill="var(--blue-dark)"/>
    <path d="M110 60 L128 78 L100 62 Z" fill="var(--blue-dark)"/>
    <text x="95" y="33" font-size="8" fill="#fff" text-anchor="middle">and <tspan font-weight="700">managing</tspan></text>
    <text x="95" y="43" font-size="8" fill="#fff" text-anchor="middle">change...</text>

    <ellipse cx="259" cy="36" rx="50" ry="31" fill="var(--blue-mid)"/>
    <path d="M235 62 L220 78 L250 64 Z" fill="var(--blue-mid)"/>
    <text x="259" y="39" font-size="8" fill="#e7f0fb" text-anchor="middle">It's about <tspan font-weight="700" fill="#fff">innovation</tspan>...</text>

    <text x="168" y="93" font-size="12.5" font-weight="800" fill="#1b1f26" text-anchor="middle">INTERPRENEURSHIP</text>

    <ellipse cx="121" cy="127" rx="42" ry="28" fill="var(--blue-dark)"/>
    <path d="M126 100 L150 96 L138 104 Z" fill="var(--blue-dark)"/>
    <text x="121" y="125" font-size="8" fill="#fff" text-anchor="middle">and <tspan font-weight="700">bearing</tspan></text>
    <text x="121" y="135" font-size="8" fill="#fff" text-anchor="middle">risk...</text>

    <ellipse cx="233" cy="139" rx="58" ry="34" fill="var(--blue-mid)"/>
    <path d="M200 110 L190 96 L214 108 Z" fill="var(--blue-mid)"/>
    <text x="233" y="131" font-size="7.8" fill="#fff" text-anchor="middle">and <tspan font-weight="700">making decisions</tspan></text>
    <text x="233" y="141" font-size="7.8" fill="#fff" text-anchor="middle">with <tspan font-weight="700">incomplete</tspan></text>
    <text x="233" y="151" font-size="7.8" fill="#fff" text-anchor="middle" font-weight="700">information...</text>
  </svg>
  <footer class="slide-footer"><div class="page-no">6</div><div class="brand"><span class="brand-dot"></span><div><div class="brand-name">Harrowby &amp; Co</div><div class="brand-tag">Accounting, Taxation &amp; Strategic Business Advisers</div></div></div><div class="footer-bar">The business improvement process – an introduction</div></footer>
</section>

<!-- 8 attitudes chart -->
<section class="slide col-r row-4">
  <header class="slide-header"><h2>Entrepreneurial attitudes</h2><p>subtitle write Here</p></header>
  <svg class="body-svg" viewBox="0 0 363 188">
    <g stroke="#c4c9d0" stroke-width=".5">
      <line x1="61" y1="45" x2="302" y2="45"/><line x1="61" y1="52" x2="302" y2="52"/>
      <line x1="61" y1="59" x2="302" y2="59"/><line x1="61" y1="66" x2="302" y2="66"/>
      <line x1="61" y1="73" x2="302" y2="73"/><line x1="61" y1="80" x2="302" y2="80"/>
      <line x1="61" y1="87" x2="302" y2="87"/><line x1="61" y1="94" x2="302" y2="94"/>
      <line x1="61" y1="101" x2="302" y2="101"/><line x1="61" y1="108" x2="302" y2="108"/>
      <line x1="61" y1="115" x2="302" y2="115"/><line x1="61" y1="122" x2="302" y2="122"/>
      <line x1="61" y1="129" x2="302" y2="129"/><line x1="61" y1="136" x2="302" y2="136"/>
    </g>
    <g fill="var(--blue)">
      <rect x="93" y="55" width="19" height="81"/>
      <rect x="128" y="82" width="19" height="54"/>
      <rect x="166" y="47" width="19" height="89"/>
      <rect x="206" y="67" width="19" height="69"/>
      <rect x="241" y="110" width="19" height="26"/>
    </g>
    <g font-size="3.6" fill="var(--ink-soft)">
      <text transform="translate(112 140) rotate(-35)" text-anchor="end">Indiv. Autonomy</text>
      <text transform="translate(140 140) rotate(-35)" text-anchor="end">Risk</text>
      <text transform="translate(184 140) rotate(-35)" text-anchor="end">Need Achievement</text>
      <text transform="translate(223 140) rotate(-35)" text-anchor="end">Simplicity</text>
      <text transform="translate(262 140) rotate(-35)" text-anchor="end">Innovativeness</text>
    </g>
  </svg>
  <footer class="slide-footer"><div class="page-no">7</div><div class="brand"><span class="brand-dot"></span><div><div class="brand-name">Harrowby &amp; Co</div><div class="brand-tag">Accounting, Taxation &amp; Strategic Business Advisers</div></div></div><div class="footer-bar">The business improvement process – an introduction</div></footer>
</section>

<!-- 9 forces -->
<section class="slide col-l row-5">
  <header class="slide-header"><h2>Forces driving change</h2><p>subtitle write Here</p></header>
  <svg class="body-svg" viewBox="0 0 363 188">
    <path d="M192 32 L236 108 L148 108 Z" fill="var(--blue)" stroke="var(--blue)" stroke-width="5" stroke-linejoin="round"/>
    <text x="192" y="91" font-size="11" font-weight="700" fill="#fff" text-anchor="middle">FIRMS</text>
    <g stroke="var(--teal)" stroke-width=".5" fill="none">
      <line x1="192" y1="23" x2="192" y2="30"/>
      <line x1="163" y1="40" x2="178" y2="52"/>
      <line x1="215" y1="40" x2="203" y2="52"/>
      <line x1="156" y1="62" x2="168" y2="68"/>
      <line x1="230" y1="62" x2="216" y2="68"/>
      <line x1="144" y1="89" x2="156" y2="89"/>
      <line x1="243" y1="89" x2="230" y2="89"/>
    </g>
    <g font-size="3.6" fill="var(--ink-soft)">
      <text x="192" y="21" text-anchor="middle">Changing Customers</text>
      <text x="157" y="31" text-anchor="middle">Increasing</text><text x="157" y="35" text-anchor="middle">Volatility</text>
      <text x="221" y="31" text-anchor="middle">Global</text><text x="221" y="35" text-anchor="middle">Competition</text>
      <text x="150" y="57" text-anchor="middle">Market</text><text x="142" y="61" text-anchor="middle">Fragmentation</text>
      <text x="230" y="57" text-anchor="middle">Government</text><text x="230" y="61" text-anchor="middle">Regulation</text>
      <text x="128" y="88" text-anchor="middle">Decreasing</text><text x="128" y="92" text-anchor="middle">Growth</text>
      <text x="258" y="88" text-anchor="middle">Technology</text><text x="258" y="92" text-anchor="middle">Changes</text>
    </g>
    <text x="52" y="122" font-size="5.2" font-weight="600" fill="var(--ink)">EXTERNAL FORCES</text>
    <line x1="52" y1="126" x2="302" y2="126" stroke="var(--teal)" stroke-width=".6" stroke-dasharray="1.5 1"/>
    <text x="52" y="134" font-size="5.2" font-weight="600" fill="var(--ink)">INTERNAL FORCES</text>
    <g stroke="var(--teal)" stroke-width=".7" fill="none">
      <circle cx="129" cy="163" r="12"/><circle cx="156" cy="163" r="12"/><circle cx="184" cy="163" r="12"/>
      <circle cx="212" cy="163" r="12"/><circle cx="239" cy="163" r="12"/>
      <path d="M135 152 L154 135 M151 135 L154 135 L154 138"/>
      <path d="M160 152 L170 135 M167 136 L170 135 L171 138"/>
      <path d="M184 151 L188 135 M185 137 L188 135 L190 138"/>
      <path d="M210 151 L206 135 M204 138 L206 135 L209 137"/>
      <path d="M234 152 L222 135 M221 138 L222 135 L225 136"/>
    </g>
    <g font-size="2.8" fill="var(--blue)" text-anchor="middle">
      <text x="129" y="162">Developing</text><text x="129" y="166">People</text>
      <text x="156" y="162">Skills</text><text x="156" y="166">Shortages</text>
      <text x="184" y="162">Poor</text><text x="184" y="166">Distribution</text>
      <text x="212" y="162">Aging</text><text x="212" y="166">Workforce</text>
      <text x="239" y="162">Workforce</text><text x="239" y="166">Diversity</text>
    </g>
  </svg>
  <footer class="slide-footer"><div class="page-no">8</div><div class="brand"><span class="brand-dot"></span><div><div class="brand-name">Harrowby &amp; Co</div><div class="brand-tag">Accounting, Taxation &amp; Strategic Business Advisers</div></div></div><div class="footer-bar">The business improvement process – an introduction</div></footer>
</section>

<!-- 10 process cycle -->
<section class="slide col-r row-5">
  <header class="slide-header"><h2>Business improvement process</h2><p>subtitle write Here</p></header>
  <svg class="body-svg" viewBox="0 0 363 188">
    <defs>
      <linearGradient id="ring" x1="0" y1="0" x2="1" y2="1">
        <stop offset="0" stop-color="var(--teal)"/><stop offset=".5" stop-color="var(--blue)"/><stop offset="1" stop-color="var(--teal)"/>
      </linearGradient>
    </defs>
    <circle cx="180" cy="97" r="56" fill="url(#ring)"/>
    <circle cx="180" cy="97" r="43" fill="#2b2d31"/>
    <g fill="#2b2d31">
      <path d="M205 50 L232 66 L222 72 Z"/>
      <path d="M227 122 L212 148 L206 138 Z"/>
      <path d="M155 144 L128 128 L138 122 Z"/>
      <path d="M133 72 L148 46 L154 56 Z"/>
    </g>
    <text x="180" y="90" font-size="7.5" fill="#fff" text-anchor="middle">Business</text>
    <text x="180" y="100" font-size="7.5" fill="#fff" text-anchor="middle">Improvement</text>
    <text x="180" y="110" font-size="7.5" fill="#fff" text-anchor="middle">Process</text>
    <g fill="#fff">
      <text x="214" y="76" font-size="8">01.</text><text x="214" y="81" font-size="4.4">Explore</text>
      <text x="192" y="146" font-size="8">02.</text><text x="192" y="151" font-size="4.4">Change</text>
      <text x="128" y="118" font-size="8">03.</text><text x="128" y="123" font-size="4.4">Grow</text>
      <text x="156" y="48" font-size="8">04.</text><text x="156" y="53" font-size="4.4">Renew</text>
    </g>
  </svg>
  <footer class="slide-footer"><div class="page-no">9</div><div class="brand"><span class="brand-dot"></span><div><div class="brand-name">Harrowby &amp; Co</div><div class="brand-tag">Accounting, Taxation &amp; Strategic Business Advisers</div></div></div><div class="footer-bar">The business improvement process – an introduction</div></footer>
</section>

</body>
</html>
```